Business card design for a Cloud Service Provider Company

We already have business card and would like to update and get a different design. Our company is Managed IT services and Cloud Solutions Company, Dorlen Systems. Attached is our current logo, current business card and sample design. I am not sure if we still need to keep our partners details on the back of the card as it does not look good to me... Please let me know if you need any additional information...

Target Market(s)

Any verticals with IT infrastructure - CEOs, CFOs and CIOs

Industry/Entity Type

Information Technology

Requirements
Must have
• First Name Last Name
• Phone
• Email address
• Company Logo

```html
<!DOCTYPE html>
<html lang="en">
<head>
<meta charset="utf-8">
<title>Dorlen Systems – Business Card</title>
<link rel="stylesheet" href="https://fonts.googleapis.com/css2?family=Rajdhani:wght@300;400;500;600;700&display=swap">
<style>
  :root {
    --ink: #333333;
    --ink-soft: #3a3a3a;
    --cyan: #00b9d8;
    --cyan-deep: #0a8fcf;
    --green: #6db33f;
    --lime: #9ccc2a;
    --dark: #2e2e2e;
    --card: #f6f6f6;
    --backdrop: #e6e6e6;
    --white: #ffffff;
  }
  * { box-sizing: border-box; margin: 0; padding: 0; }
  html, body {
    width: 1000px;
    height: 1200px;
    overflow: hidden;
    background: var(--backdrop);
    font-family: "Rajdhani", sans-serif;
    color: var(--ink);
  }
  .canvas { position: relative; width: 1000px; height: 1200px; }

  .card {
    position: absolute;
    left: 0;
    width: 1000px;
    background: var(--card);
    box-shadow: 0 3px 8px rgba(0,0,0,0.25);
    overflow: hidden;
  }
  .card--front { top: 19px; height: 571px; }
  .card--back  { top: 609px; height: 576px; }

  /* edge colour strips */
  .edge-strip {
    position: absolute;
    top: 0;
    width: 27px;
    height: 100%;
    display: flex;
    flex-direction: column;
  }
  .edge-strip--left { left: 0; }
  .edge-strip--right { right: 0; }
  .edge-strip span { display: block; width: 100%; }
  .strip-dark  { background: var(--dark); }
  .strip-green { background: var(--green); }
  .strip-cyan  { background: var(--cyan); flex: 1; }

  /* front */
  .brand {
    position: absolute;
    top: 210px;
    left: 0;
    width: 100%;
    display: flex;
    justify-content: center;
    align-items: center;
    gap: 18px;
  }
  .brand-dot {
    width: 34px;
    height: 34px;
    border-radius: 50%;
    background: var(--cyan);
  }
  .brand-name {
    font-size: 84px;
    font-weight: 600;
    color: var(--ink);
    line-height: 1;
  }
  .company-details {
    position: absolute;
    top: 405px;
    left: 0;
    width: 100%;
    text-align: center;
    font-size: 29px;
    font-weight: 600;
    line-height: 35px;
    color: var(--ink-soft);
    font-style: normal;
  }

  /* back */
  .mark-area {
    position: absolute;
    left: 0;
    top: 0;
    width: 420px;
    height: 100%;
    background: linear-gradient(150deg, rgba(156,204,42,0.35) 0%, rgba(10,143,207,0.35) 55%, rgba(156,204,42,0.3) 100%);
  }
  .name-band {
    position: absolute;
    top: 78px;
    left: 424px;
    width: 549px;
    height: 139px;
    background: var(--cyan);
    clip-path: polygon(40px 0, 100% 0, 100% 100%, 0 100%);
  }
  .person {
    position: absolute;
    top: 92px;
    right: 57px;
    text-align: right;
    color: var(--white);
  }
  .person-name {
    font-size: 50px;
    font-weight: 700;
    line-height: 56px;
    white-space: nowrap;
  }
  .person-title {
    font-size: 42px;
    font-weight: 400;
    line-height: 40px;
    letter-spacing: 0.5px;
    white-space: nowrap;
  }
  .contact-list {
    position: absolute;
    top: 262px;
    right: 38px;
    list-style: none;
  }
  .contact-item {
    display: flex;
    justify-content: flex-end;
    align-items: center;
    height: 52px;
    gap: 16px;
  }
  .contact-text {
    font-size: 38px;
    color: var(--ink);
    white-space: nowrap;
  }
  .contact-text--email { font-weight: 400; font-size: 38px; }
  .contact-text--phone { font-weight: 600; }
  .contact-icon {
    width: 39px;
    height: 39px;
    border-radius: 50%;
    background: var(--cyan-deep);
    color: var(--white);
    font-size: 30px;
    font-weight: 500;
    display: flex;
    align-items: center;
    justify-content: center;
    line-height: 1;
  }
</style>
</head>
<body>
<main class="canvas">

  <section class="card card--front">
    <div class="edge-strip edge-strip--left">
      <span class="strip-dark" style="height:29px"></span>
      <span class="strip-green" style="height:48px"></span>
      <span class="strip-cyan"></span>
      <span class="strip-green" style="height:48px"></span>
      <span class="strip-dark" style="height:33px"></span>
    </div>
    <div class="edge-strip edge-strip--right">
      <span class="strip-dark" style="height:29px"></span>
      <span class="strip-green" style="height:48px"></span>
      <span class="strip-cyan"></span>
      <span class="strip-green" style="height:48px"></span>
      <span class="strip-dark" style="height:33px"></span>
    </div>

    <div class="brand">
      <span class="brand-name">Dorlen Systems</span>
      <span class="brand-dot"></span>
    </div>

    <address class="company-details">
      <p>Level 14, 88 Harbour Lane Sydney, NSW 2000</p>
      <p>www.dorlensystems.com.au</p>
      <p>Support : 1300 555 210</p>
    </address>
  </section>

  <section class="card card--back">
    <div class="mark-area" role="img" aria-label="Large brand symbol decoration in blue and green"></div>

    <div class="edge-strip edge-strip--right">
      <span class="strip-dark" style="height:30px"></span>
      <span class="strip-green" style="height:46px"></span>
      <span class="strip-cyan"></span>
      <span class="strip-green" style="height:48px"></span>
      <span class="strip-dark" style="height:38px"></span>
    </div>

    <div class="name-band"></div>
    <div class="person">
      <h1 class="person-name">MARCUS T. HALLOWAY</h1>
      <p class="person-title">TECHNICAL MANAGER</p>
    </div>

    <ul class="contact-list">
      <li class="contact-item">
        <span class="contact-text contact-text--email">marcus@dorlensystems.com.au</span>
        <span class="contact-icon">@</span>
      </li>
      <li class="contact-item">
        <span class="contact-text contact-text--phone">+61 2 5550 1234</span>
        <span class="contact-icon">P</span>
      </li>
      <li class="contact-item">
        <span class="contact-text contact-text--phone">+61 455501982</span>
        <span class="contact-icon">M</span>
      </li>
    </ul>
  </section>

</main>
</body>
</html>
```